Coach needs thank you cards (business card format) to deliver to customers. Model behavior

I am a coach who needs thank-you cards for customers and people to appreciate "exemplary behavior". First and foremost it is about the mindfulness of the people who have a great behavior to estimate and reward. The colors should contain silver and light like the logo of Mentorbrightpath.
Updates

The following should include the cards front and back. Front: Praise for: there should be room below to enter the name of the person. The fangs should be silver and light blue as on the logo which I have uploaded. Back: capitalized by date: exemplary behavior should be at the bottom right. mentorbrightpath.ch

```html
<!DOCTYPE html>
<html lang="en">
<head>
<meta charset="utf-8">
<title>Mentorbrightpath thank-you card</title>
<link rel="stylesheet" href="https://fonts.googleapis.com/css2?family=Arimo:wght@700&family=Lato:wght@400&display=swap">
<style>
  :root {
    --canvas: #dcdcdc;
    --card-white: #ffffff;
    --brand-blue: #1f6fba;
    --back-blue: #2273bb;
    --pattern-blue: #2e7cc2;
    --soft-blue: #a9c8e6;
    --silver: #9a9a9a;
    --text-dark: #3a3a3a;
    --line-light: rgba(255, 255, 255, 0.75);
  }
  html, body {
    margin: 0;
    padding: 0;
    width: 1200px;
    height: 900px;
    overflow: hidden;
    background: var(--canvas);
  }
  .stage {
    position: relative;
    width: 1200px;
    height: 900px;
  }
  .card {
    position: absolute;
    top: 306px;
    width: 439px;
    height: 271px;
    border-radius: 12px;
    overflow: hidden;
  }
  .card-front {
    left: 149px;
    background: var(--card-white);
  }
  .card-back {
    left: 609px;
    background: var(--back-blue);
  }
  .brand-mark {
    position: absolute;
    left: 76px;
    top: 77px;
    width: 70px;
    height: 70px;
    border-radius: 50%;
    border: 2px solid var(--soft-blue);
    box-sizing: border-box;
  }
  .brand-name {
    position: absolute;
    left: 0;
    width: 222px;
    top: 155px;
    text-align: center;
    font-family: "Lato", sans-serif;
    font-size: 19px;
    color: var(--brand-blue);
    letter-spacing: -0.2px;
  }
  .divider {
    position: absolute;
    left: 215px;
    top: 78px;
    width: 1px;
    height: 112px;
    background: var(--silver);
  }
  .contact {
    position: absolute;
    left: 228px;
    top: 80px;
  }
  .person-name {
    margin: 0;
    font-family: "Arimo", sans-serif;
    font-weight: 700;
    font-size: 13.8px;
    line-height: 17px;
    color: var(--brand-blue);
    letter-spacing: 0;
    white-space: nowrap;
  }
  .address {
    margin: 9px 0 0;
    font-family: "Lato", sans-serif;
    font-size: 12.5px;
    color: var(--text-dark);
  }
  .contact-list {
    list-style: none;
    margin: 19px 0 0;
    padding: 0;
    font-family: "Lato", sans-serif;
    font-size: 12.5px;
    color: var(--text-dark);
  }
  .contact-list li {
    display: flex;
    align-items: center;
    height: 17px;
  }
  .contact-icon {
    width: 13px;
    height: 13px;
    margin-right: 2px;
    flex: none;
  }
  .praise {
    position: absolute;
    left: 30px;
    right: 30px;
    top: 222px;
    display: flex;
    align-items: flex-end;
    font-family: "Lato", sans-serif;
    font-size: 12px;
    color: var(--silver);
  }
  .praise-line {
    flex: 1;
    margin-left: 8px;
    border-bottom: 1px solid var(--soft-blue);
    height: 12px;
  }
  .back-pattern {
    position: absolute;
    inset: 0;
    background: radial-gradient(circle at 50% 40%, var(--pattern-blue), var(--back-blue));
  }
  .back-name {
    position: absolute;
    left: 0;
    right: 0;
    top: 100px;
    text-align: center;
    font-family: "Lato", sans-serif;
    font-size: 15px;
    color: var(--card-white);
  }
  .back-note {
    position: absolute;
    right: 22px;
    bottom: 20px;
    width: 170px;
    font-family: "Lato", sans-serif;
    font-size: 11px;
    color: var(--card-white);
    text-align: right;
  }
  .date-row {
    display: flex;
    align-items: flex-end;
  }
  .date-line {
    flex: 1;
    margin-left: 6px;
    border-bottom: 1px solid var(--line-light);
    height: 11px;
  }
  .behavior {
    margin-top: 7px;
    font-family: "Arimo", sans-serif;
    font-weight: 700;
    font-size: 11px;
    letter-spacing: 1px;
  }
</style>
</head>
<body>
<main class="stage">
  <section class="card card-front">
    <div class="brand-mark"></div>
    <div class="brand-name">Mentorbrightpath</div>
    <div class="divider"></div>
    <div class="contact">
      <h1 class="person-name">LUKAS PETER BRANDNER</h1>
      <p class="address">Seeblick 22&nbsp; 6300 Zug</p>
      <ul class="contact-list">
        <li>
          <svg class="contact-icon" viewBox="0 0 14 14" aria-hidden="true">
            <circle cx="7" cy="7" r="6.5" fill="var(--brand-blue)"/>
            <path d="M3.5 6.5c0-1.5 7-1.5 7 0l-1 .8-1-.6v-.6H5.5v.6l-1 .6z M5 7.5h4l1 2.5H4z" fill="#fff"/>
          </svg>
          4179 555 01 23
        </li>
        <li>
          <svg class="contact-icon" viewBox="0 0 14 14" aria-hidden="true">
            <circle cx="7" cy="7" r="6.5" fill="var(--brand-blue)"/>
            <rect x="3.5" y="4.5" width="7" height="5" fill="#fff"/>
            <path d="M3.5 4.5L7 7.3l3.5-2.8" fill="none" stroke="var(--brand-blue)" stroke-width="0.8"/>
          </svg>
          change@mentorbrightpath.ch
        </li>
        <li>
          <svg class="contact-icon" viewBox="0 0 14 14" aria-hidden="true">
            <circle cx="7" cy="7" r="6.5" fill="var(--brand-blue)"/>
            <circle cx="7" cy="7" r="3.6" fill="none" stroke="#fff" stroke-width="1"/>
            <path d="M3.4 7h7.2M7 3.4c-1.6 2-1.6 5.2 0 7.2M7 3.4c1.6 2 1.6 5.2 0 7.2" fill="none" stroke="#fff" stroke-width="0.7"/>
          </svg>
          www.mentorbrightpath.ch
        </li>
      </ul>
    </div>
    <div class="praise">
      <span>Praise for:</span>
      <span class="praise-line"></span>
    </div>
  </section>

  <section class="card card-back">
    <div class="back-pattern" role="img" aria-label="Faint repeating pattern of compass emblems on blue"></div>
    <div class="back-name">Mentorbrightpath</div>
    <div class="back-note">
      <div class="date-row"><span>Date:</span><span class="date-line"></span></div>
      <div class="behavior">EXEMPLARY BEHAVIOR</div>
    </div>
  </section>
</main>
</body>
</html>
```